UK landscaping company needs website

We, Brindle Landscapes need a website design for a company based in Surrey, UK. The design should be bold and playful. We have three main areas of work driveways, paving and fencing. It shouldn't be too heavy in text and concentrate on the pictures from previous jobs we've completed. You may use stock images for the design, these can be changed if you are successful. Please don’t just copy the flyer it is just there to provide content.
We have a logo design which we would also like editing slightly.
Here are some of my local competitors
https://www.vexmoorlandscapes.co.uk/

https://www.twinreedgardendesign.com/

https://quarnelllandscapes.co.uk/

Industry/Entity Type

Landscaping

Coding

Coded - Design and coding required

Number of Pages Required

3 page

Font styles to use
Sans Serif

Requirements
Must have
• Pictures of my previous jobs.
Must be mobile friendly
Easy to navigate
Nice to have
• Try to use different colours. It would be good to have some designs that aren’t just black and green.
I’d like some curves in the design.
Should not have
• We install hard landscaping. Think more building/construction and less plants and cutting grass.

```html
<!DOCTYPE html>
<html lang="en">
<head>
<meta charset="utf-8">
<title>Brindle Landscapes</title>
<link rel="stylesheet" href="https://fonts.googleapis.com/css2?family=Montserrat:wght@500;600;700;800&family=Nunito:wght@400;600;700;800&display=swap">
<style>
:root{
  --sky:#abe7fd;
  --green:#6cbf3c;
  --green-deep:#5ea92b;
  --black:#000;
  --charcoal:#2b2b2b;
  --white:#fff;
  --ink:#111;
  --text:#444;
  --muted:#888;
  --line:#ddd;
}
*{box-sizing:border-box;margin:0;padding:0}
html,body{width:1200px;height:4000px;overflow:hidden;background:var(--sky)}
body{position:relative;font-family:"Nunito",sans-serif;color:var(--text)}
.abs{position:absolute}
.page{position:absolute;left:68px;top:202px;width:1065px;height:3596px;background:var(--white)}

/* header */
.site-header{position:absolute;left:68px;top:202px;width:1065px;height:99px;background:var(--black)}
.brand{position:absolute;left:130px;top:30px;color:var(--white);font-family:"Montserrat",sans-serif;font-weight:700;font-size:26px;letter-spacing:1px;display:flex;align-items:center;gap:10px}
.brand .dot{width:14px;height:14px;border-radius:50%;background:var(--green)}
.main-nav{position:absolute;left:472px;top:68px;display:flex;gap:0;font-family:"Montserrat",sans-serif;font-size:10px;font-weight:600;color:var(--white)}
.main-nav span{position:absolute;white-space:nowrap}
.main-nav .active{color:var(--green)}
.btn-contact{position:absolute;left:821px;top:50px;width:128px;height:32px;border-radius:16px;background:var(--green);color:var(--white);font-family:"Montserrat",sans-serif;font-size:9px;font-weight:700;display:flex;align-items:center;justify-content:center}

/* hero */
.hero{position:absolute;left:68px;top:301px;width:1065px;height:600px;background:linear-gradient(180deg,#b9cf6a 0%,#8fba3a 40%,#6aa12b 75%,#9a9380 100%)}

/* services */
.service{position:absolute;top:804px;width:269px;height:236px;background:var(--green);color:var(--white);text-align:center}
.service .icon{position:absolute;left:88px;top:-47px;width:94px;height:94px;border-radius:50%;background:var(--white);display:flex;align-items:center;justify-content:center}
.service h3{position:absolute;left:0;right:0;top:52px;font-family:"Montserrat",sans-serif;font-weight:700;font-size:29px}
.service p{position:absolute;left:18px;right:18px;top:98px;font-size:11px;line-height:16.5px}
.service .more{position:absolute;left:72px;top:218px;width:126px;height:34px;border-radius:17px;background:var(--white);border:2px solid var(--green);color:var(--green);font-family:"Montserrat",sans-serif;font-weight:700;font-size:11px;display:flex;align-items:center;justify-content:center}

/* about */
.about-media{position:absolute;left:174px;top:1180px;width:337px;height:421px;border:4px solid var(--green);background:var(--white)}
.about-media .ph{position:absolute;left:2px;right:2px}
.about-label{position:absolute;left:553px;top:1190px;font-family:"Montserrat",sans-serif;font-size:11px;font-weight:700;color:var(--green);border-bottom:1px solid var(--green);padding-bottom:2px;width:66px}
.about-title{position:absolute;left:556px;top:1216px;font-family:"Montserrat",sans-serif;font-weight:700;font-size:30px;color:var(--ink)}
.about-copy{position:absolute;left:562px;top:1278px;width:450px;font-size:11.3px;line-height:16.5px;color:#333}
.about-copy p{margin-bottom:17px}
.stats{position:absolute;left:568px;top:1518px;display:flex;gap:0}
.stat{position:absolute;display:flex;gap:12px;align-items:flex-start}
.stat .ic{width:34px;height:34px;border-radius:50%;background:var(--green);display:flex;align-items:center;justify-content:center}
.stat b{display:block;font-size:11px;color:#222;font-weight:700;border-bottom:2px solid var(--green);width:14px;white-space:nowrap;padding-bottom:3px}
.stat small{display:block;font-size:6px;color:var(--muted);margin-top:6px;white-space:nowrap}

/* projects */
.projects{position:absolute;left:68px;top:1702px;width:1065px;height:795px;background:var(--charcoal)}
.projects h2{position:absolute;left:48px;top:30px;font-family:"Montserrat",sans-serif;font-weight:800;font-size:33px;color:var(--green)}
.filter{position:absolute;top:49px;height:26px;border-radius:13px;border:2px solid var(--green);color:var(--white);font-family:"Montserrat",sans-serif;font-size:10px;font-weight:700;display:flex;align-items:center;padding-left:10px}
.filter.on{background:var(--green);justify-content:center;padding:0}
.projects .rule{position:absolute;left:59px;top:88px;width:955px;height:3px;background:var(--green)}
.tile{position:absolute;width:309px;height:308px}

/* faq + form */
.sec-title{position:absolute;top:2628px;font-family:"Montserrat",sans-serif;font-weight:600;font-size:20px;color:var(--ink)}
.sec-title::after{content:"";position:absolute;left:0;top:34px;width:26px;height:2px;background:var(--green)}
.acc{position:absolute;left:267px;width:309px;height:28px;border-radius:14px;background:var(--green);color:var(--white);font-size:7.5px;font-weight:700;display:flex;align-items:center;justify-content:space-between;padding:0 14px}
.acc.open{background:#222}
.acc i{font-style:normal;font-size:15px;font-weight:400}
.acc-body{position:absolute;left:283px;top:2766px;width:280px;font-size:7.5px;line-height:13px;color:var(--muted)}
.field{position:absolute;border:1px solid var(--line);border-radius:3px;font-size:7px;color:var(--muted);padding:7px 10px}
.submit{position:absolute;left:826px;top:2885px;width:90px;height:24px;border-radius:12px;background:var(--green);color:var(--white);font-size:7px;font-weight:700;display:flex;align-items:center;justify-content:center}

/* testimonial */
.family{position:absolute;left:68px;top:3075px;width:531px;height:265px;background:linear-gradient(120deg,#7aa84a,#c9d9a0 45%,#9dbb6d 70%,#d7c7a6)}
.review{position:absolute;left:599px;top:3075px;width:534px;height:265px;background:var(--charcoal);color:var(--white)}
.review h3{position:absolute;left:28px;top:48px;font-family:"Montserrat",sans-serif;font-weight:600;font-size:19px}
.avatar{position:absolute;left:38px;top:116px;width:56px;height:56px;border-radius:50%;background:linear-gradient(#c9a88a,#7b5a44);border:3px solid #555}
.review .who{position:absolute;left:114px;top:122px;font-size:8.5px;color:var(--green)}
.review .role{position:absolute;left:114px;top:140px;font-size:7px;color:#bbb}
.review .quote{position:absolute;left:114px;top:160px;width:240px;font-size:7px;line-height:12px;color:#ddd}
.review .mark{position:absolute;left:313px;top:114px;font-size:26px;color:#777;font-family:Georgia,serif}
.dots{position:absolute;left:114px;top:210px;display:flex;gap:6px}
.dots span{width:16px;height:4px;border-radius:2px;border:1px solid #888}
.dots .on{background:var(--green);border-color:var(--green)}

/* emergency band */
.band{position:absolute;left:68px;top:3421px;width:1065px;height:96px;background:#6dae1f;overflow:hidden}
.band .ph{position:absolute;left:0;top:0;width:520px;height:96px;background:linear-gradient(90deg,#5a3b27,#8a5a36 60%,#b59b46 88%,#6dae1f);clip-path:polygon(0 0,100% 0,92% 100%,0 100%)}
.band p{position:absolute;left:507px;top:21px;font-size:12.5px;line-height:16px;color:var(--white)}
.band .tel{position:absolute;left:507px;top:57px;font-family:"Montserrat",sans-serif;font-weight:700;font-size:16px;color:var(--white);letter-spacing:1px;display:flex;gap:8px;align-items:center}

/* footer */
.site-footer{position:absolute;left:68px;top:3528px;width:1065px;height:270px;background:var(--black);color:var(--white)}
.foot-brand{position:absolute;left:215px;top:82px;font-family:"Montserrat",sans-serif;font-weight:700;font-size:30px;display:flex;align-items:center;gap:12px}
.foot-brand .dot{width:18px;height:18px;border-radius:50%;background:var(--green)}
.contacts{position:absolute;left:500px;top:75px;font-family:"Montserrat",sans-serif;font-weight:600;font-size:24px;line-height:30px}
.contacts div{display:flex;align-items:center;gap:10px}
.foot-nav{position:absolute;top:213px;left:0;font-family:"Montserrat",sans-serif;font-weight:600;font-size:19px}
.foot-nav span{position:absolute;white-space:nowrap}
.foot-nav .active{color:var(--green)}
</style>
</head>
<body>
<div class="page"></div>

<header class="site-header">
  <div class="brand"><span class="dot"></span>Brindle Landscapes</div>
  <nav class="main-nav">
    <span class="active" style="left:68px">Home</span>
    <span style="left:118px">Our Services</span>
    <span style="left:203px">About Us</span>
    <span style="left:280px">Our Projects</span>
    <span style="left:358px">FAQ</span>
  </nav>
  <div class="btn-contact">Contact Us Today</div>
</header>

<div class="hero" role="img" aria-label="Sunlit landscaped garden with rolling lawn, brick paved path and sprinklers"></div>

<section class="service" style="left:193px">
  <div class="icon"><svg width="48" height="40" viewBox="0 0 48 40"><path d="M40 6 C20 4 10 12 24 18 C38 24 26 34 6 34" fill="none" stroke="#000" stroke-width="9" stroke-linecap="round"/><path d="M40 6 C20 4 10 12 24 18 C38 24 26 34 6 34" fill="none" stroke="#fff" stroke-width="1.5" stroke-dasharray="3 3"/></svg></div>
  <h3>Driveways</h3>
  <p>Lorem ipsum dolor sit amet, consectetur adipiscing elit, sed do eiusmod tempor incididunt ut labore et dolore magna aliqua. Quis ipsum suspendisse ultrices gravida. Risus commodo viverra maecenas accumsan lacus vel facilisis.</p>
  <div class="more">Read More</div>
</section>
<section class="service" style="left:466px">
  <div class="icon"><svg width="50" height="36" viewBox="0 0 50 36"><rect x="2" y="8" width="46" height="4" fill="#000"/><rect x="2" y="26" width="46" height="4" fill="#000"/><g fill="#000"><rect x="3" y="3" width="4" height="32"/><rect x="10" y="3" width="4" height="32"/><rect x="17" y="3" width="4" height="32"/><rect x="24" y="3" width="4" height="32"/><rect x="31" y="3" width="4" height="32"/><rect x="38" y="3" width="4" height="32"/><rect x="44" y="3" width="4" height="32"/></g></svg></div>
  <h3>Fencing</h3>
  <p>Lorem ipsum dolor sit amet, consectetur adipiscing elit, sed do eiusmod tempor incididunt ut labore et dolore magna aliqua. Quis ipsum suspendisse ultrices gravida. Risus commodo viverra maecenas accumsan lacus vel facilisis.</p>
  <div class="more">Read More</div>
</section>
<section class="service" style="left:741px">
  <div class="icon"><svg width="40" height="40" viewBox="0 0 40 40"><rect x="2" y="2" width="36" height="36" fill="none" stroke="#000" stroke-width="3"/><g stroke="#000" stroke-width="3"><path d="M2 20 L20 2 M2 38 L38 2 M20 38 L38 20 M2 20 L20 38 M2 2 L38 38 M20 2 L38 20"/></g></svg></div>
  <h3>Paving</h3>
  <p>Lorem ipsum dolor sit amet, consectetur adipiscing elit, sed do eiusmod tempor incididunt ut labore et dolore magna aliqua. Quis ipsum suspendisse ultrices gravida. Risus commodo viverra maecenas accumsan lacus vel facilisis.</p>
  <div class="more">Read More</div>
</section>

<div class="about-media">
  <div class="ph" role="img" aria-label="Garden before work, overgrown beds" style="top:2px;height:196px;background:linear-gradient(160deg,#3e4a2c,#6b7a46 50%,#8a7c5c)"></div>
  <div class="ph" role="img" aria-label="Garden after work, new striped lawn and paved edging" style="top:201px;height:210px;background:linear-gradient(180deg,#4f6b34,#5c9a36 40%,#7fb14a)"></div>
</div>
<div class="about-label">About US</div>
<h2 class="about-title">Welcome To Brindle Landscapes</h2>
<div class="about-copy">
  <p>Lorem ipsum dolor sit amet, consectetur adipiscing elit, sed do eiusmod tempor incididunt ut labore et dolore magna aliqua. Quis ipsum suspendisse ultrices gravida. Risus commodo viverra maecenas accumsan lacus vel facilisis.</p>
  <p>Lorem ipsum dolor sit amet, consectetur adipiscing elit, sed do eiusmod tempor incididunt ut labore et dolore magna aliqua. Quis ipsum suspendisse ultrices gravida. Risus commodo viverra maecenas accumsan lacus vel facilisis.</p>
  <p>Lorem ipsum dolor sit amet, consectetur adipiscing elit, sed do eiusmod tempor incididunt ut labore et dolore magna aliqua. Quis ipsum suspendisse ultrices gravida. Risus commodo viverra maecenas accumsan lacus vel facilisis.</p>
</div>
<div class="stats">
  <div class="stat" style="left:0"><span class="ic"><svg width="14" height="14" viewBox="0 0 14 14"><circle cx="7" cy="7" r="6" fill="none" stroke="#fff" stroke-width="1.3"/><path d="M4 8 Q7 11 10 8" fill="none" stroke="#fff" stroke-width="1.3"/></svg></span><div><b>1900</b><small>Happy Clients</small></div></div>
  <div class="stat" style="left:103px"><span class="ic"><svg width="12" height="14" viewBox="0 0 12 14"><path d="M2 1 H10 V13 L6 10 L2 13 Z" fill="none" stroke="#fff" stroke-width="1.3"/></svg></span><div><b>1900</b><small>Receive Awards</small></div></div>
  <div class="stat" style="left:203px"><span class="ic"><svg width="14" height="14" viewBox="0 0 14 14"><rect x="1" y="1" width="12" height="12" fill="none" stroke="#fff" stroke-width="1.3"/><path d="M1 7 H13 M7 1 V13" stroke="#fff" stroke-width="1.3"/></svg></span><div><b>2500</b><small>Finished Work</small></div></div>
</div>

<section class="projects">
  <h2>OUR PROJECTS</h2>
  <div class="filter on" style="left:398px;width:82px">ALL</div>
  <div class="filter" style="left:490px;width:86px">Driveways</div>
  <div class="filter" style="left:583px;width:86px">Fencing</div>
  <div class="filter" style="left:676px;width:86px">Paving</div>
  <svg class="abs" style="left:927px;top:52px" width="90" height="20" viewBox="0 0 90 20"><path d="M32 10 H2 M10 2 L2 10 L10 18 M58 10 H88 M80 2 L88 10 L80 18" fill="none" stroke="#fff" stroke-width="2"/></svg>
  <div class="rule"></div>
  <div class="tile" role="img" aria-label="Timber fence with sleeper steps and patio" style="left:59px;top:127px;background:linear-gradient(180deg,#8aa0b5 0%,#6a5440 25%,#5b4532 55%,#4f8a2a 75%,#b9b3a6)"></div>
  <div class="tile" role="img" aria-label="Garden before and after turfing" style="left:382px;top:127px;background:linear-gradient(180deg,#445232,#6c7a4c 48%,#e6e6e6 48.5%,#e6e6e6 49.5%,#55903a 50%,#79b04d)"></div>
  <div class="tile" role="img" aria-label="Grey stone slab path beside lawn" style="left:705px;top:127px;background:linear-gradient(135deg,#6aa23a 0%,#6aa23a 25%,#c9c9c5 40%,#aeaeaa 75%,#6b5a4a)"></div>
  <div class="tile" role="img" aria-label="Timber pergola over pale patio with lawn" style="left:59px;top:452px;background:linear-gradient(160deg,#9a5a3c,#7a5a3e 35%,#3f7a2a 60%,#d8d8d4)"></div>
  <div class="tile" role="img" aria-label="Timber pergola over a seating area" style="left:382px;top:452px;background:linear-gradient(180deg,#cfd6dc,#b8a88a 30%,#6b5a44 60%,#c0b8aa)"></div>
  <div class="tile" role="img" aria-label="Block paved driveway in brindle tones" style="left:705px;top:452px;background:linear-gradient(150deg,#6a5a56,#8a6a62 40%,#7a6a70 70%,#5a4a48)"></div>
</section>

<h3 class="sec-title" style="left:267px">Frequently Asked Question</h3>
<h3 class="sec-title" style="left:599px">Request An Estimate</h3>
<div class="acc" style="top:2685px">01. Rerspiciatis unde omnis iste natus erty?<i>+</i></div>
<div class="acc open" style="top:2717px">02. Sed ut perspiciatis unde omnis iste natus error?<i>–</i></div>
<p class="acc-body">Sed ut perspiciatis unde omnis iste natus error sit voluptatem accusa nt ium dolorem que laudantium totam rem aperiamSed ut perspiciatis unde omnis iste natus error sit voluptatem accusa nt ium dolorem que laudantium totam rem aperiamue laudantium totam rem aperiamSed ut perspiciatis unde omnis istety.</p>
<div class="acc" style="top:2849px">03. Unde omnis iste natused perspiciatis ?<i>+</i></div>
<div class="acc" style="top:2881px">04. Sedperspiciatis unde omnis ister?<i>+</i></div>

<div class="field" style="left:601px;top:2685px;width:150px;height:25px">Name*</div>
<div class="field" style="left:764px;top:2685px;width:152px;height:25px">E-mail*</div>
<div class="field" style="left:601px;top:2725px;width:315px;height:25px">Select Subject<svg class="abs" style="right:10px;top:11px" width="6" height="4" viewBox="0 0 6 4"><path d="M0 0 H6 L3 4Z" fill="#666"/></svg></div>
<div class="field" style="left:601px;top:2766px;width:315px;height:102px">Message</div>
<div class="submit">SUBMIT</div>

<div class="family" role="img" aria-label="Family planting flowers together in a garden"></div>
<section class="review">
  <h3>What Client's Say</h3>
  <div class="avatar" role="img" aria-label="Client portrait"></div>
  <div class="who">Daniel Marsh</div>
  <div class="role">CEO</div>
  <p class="quote">Lorem ipsum dolor sit amet, consectetur elit, loremosCurabitur euismod enim a metus adipiscing aliquam.</p>
  <div class="mark">“</div>
  <div class="dots"><span></span><span class="on"></span><span></span></div>
</section>

<div class="band">
  <div class="ph" role="img" aria-label="Garden tools and watering can on a wooden table"></div>
  <p>If you have an gardner need, simply call our<br>24 hour emergecny number</p>
  <div class="tel"><svg width="14" height="14" viewBox="0 0 24 24"><path d="M6.6 10.8a15 15 0 006.6 6.6l2.2-2.2a1 1 0 011-.25 11.4 11.4 0 003.6.57 1 1 0 011 1V20a1 1 0 01-1 1A17 17 0 013 4a1 1 0 011-1h3.5a1 1 0 011 1c0 1.25.2 2.45.57 3.57a1 1 0 01-.25 1z" fill="#fff"/></svg>+ 123 456 78910</div>
</div>

<footer class="site-footer">
  <div class="foot-brand"><span class="dot"></span>Brindle<br>Landscapes</div>
  <div class="contacts">
    <div><svg width="18" height="18" viewBox="0 0 24 24"><circle cx="12" cy="12" r="10.5" fill="none" stroke="#fff" stroke-width="1.6"/><path d="M8.5 7.5l2 2-1 1.5a7 7 0 003.5 3.5l1.5-1 2 2-1.5 1.5A8 8 0 017 9z" fill="#fff"/></svg>07700 900 482</div>
    <div><svg width="18" height="18" viewBox="0 0 24 24"><circle cx="12" cy="12" r="10.5" fill="none" stroke="#fff" stroke-width="1.6"/><rect x="6.5" y="8" width="11" height="8" fill="none" stroke="#fff" stroke-width="1.4"/><path d="M6.5 8l5.5 4.5L17.5 8" fill="none" stroke="#fff" stroke-width="1.4"/></svg>info@brindle-landscapes.com</div>
    <div><svg width="18" height="18" viewBox="0 0 24 24"><circle cx="12" cy="12" r="10.5" fill="none" stroke="#fff" stroke-width="1.6"/><path d="M3 12h18M12 2c-4 4-4 16 0 20M12 2c4 4 4 16 0 20" fill="none" stroke="#fff" stroke-width="1.4"/></svg>brindle-landscapes.com</div>
  </div>
  <nav class="foot-nav">
    <span class="active" style="left:224px">Home</span>
    <span style="left:325px">Our Services</span>
    <span style="left:489px">About Us</span>
    <span style="left:643px">Our Projects</span>
    <span style="left:800px">FAQ</span>
  </nav>
</footer>
</body>
</html>
```